Surface Protection company needs cards

We are a New Zealand company that will apply nanotechnology coatings on surfaces to prevent growth and spread of bacteria, viruses, mold etc with a sprayer. We deal with large corporates, airlines, hospitals and schools so we are after a new modern, simple and clean look that will have great visual impact.
We a company that is focused on prevention and protection.

Company name, Vela Shield

Subtext, Antimicrobial Surface Protection

Logo, VS

Target Market(s)

Hospitals, Transport agencies, Airlines, Corporate entities

Contact Information for Business Card

Company name, VelaShield
Logo, VS

Gareth Tolley
velashieldnz@postbox.example
+64219305562
www.velashield.example.nz

Requirements
Must have
• Simple clean look.
Nice to have
• We apply nano coatings so try and incorporate this into a theme somehow

```html
<!DOCTYPE html>
<html lang="en">
<head>
<meta charset="utf-8">
<title>Vela Shield — Business Card</title>
<link rel="stylesheet" href="https://fonts.googleapis.com/css2?family=Montserrat:wght@400;500&family=Open+Sans:wght@400&display=swap">
<style>
  :root {
    --page: #ffffff;
    --ink: #111111;
    --band-dark: #1c1c1c;
    --silver: #d9d9d9;
    --mist: #c9c9c9;
    --mist-light: #d2d2d2;
    --sky: #93aebf;
    --sky-light: #a3bccb;
  }
  * { box-sizing: border-box; margin: 0; padding: 0; }
  html, body {
    width: 939px; height: 1200px; overflow: hidden;
    background: var(--page);
  }
  .sheet { position: relative; width: 939px; height: 1200px; }
  .card {
    position: absolute; left: 20px; width: 893px; height: 547px;
    overflow: hidden; background: var(--page);
  }
  .card--front { top: 25px; }
  .card--back { top: 623px; }

  .texture { position: absolute; left: 0; width: 100%; }
  .texture--mist {
    top: 0; height: 154px;
    background: linear-gradient(180deg, var(--mist-light), var(--mist));
  }
  .texture--sky {
    bottom: 0; height: 136px;
    background: linear-gradient(90deg, var(--sky-light), var(--sky) 50%, var(--sky-light));
  }
  .texture--fade {
    bottom: 0; height: 155px;
    background: linear-gradient(180deg, var(--mist) 0%, var(--mist-light) 45%, var(--sky) 100%);
  }

  .brand-band {
    position: absolute; top: 154px; left: 0; width: 100%; height: 257px;
    background: var(--band-dark);
    display: flex; flex-direction: column; align-items: center; justify-content: center;
    color: var(--silver);
  }
  .brand-mark {
    font-family: "Montserrat", sans-serif; font-weight: 400;
    font-size: 84px; line-height: 1; letter-spacing: 2px;
    margin-bottom: 18px;
  }
  .brand-name {
    font-family: "Montserrat", sans-serif; font-weight: 400;
    font-size: 45px; line-height: 1; letter-spacing: 1px;
    margin-bottom: 20px;
  }
  .brand-tagline {
    font-family: "Open Sans", sans-serif; font-weight: 400;
    font-size: 21px; letter-spacing: 1px;
  }

  .contact {
    position: absolute; top: 60px; right: 50px;
    text-align: right; color: var(--ink);
    font-family: "Montserrat", sans-serif; font-weight: 400;
  }
  .contact__mark {
    font-size: 96px; line-height: 1; letter-spacing: 2px;
    margin-bottom: 38px;
  }
  .contact__line {
    font-size: 23px; line-height: 42px; letter-spacing: 1.6px;
  }
</style>
</head>
<body>
<main class="sheet">
  <section class="card card--front">
    <div class="texture texture--mist" role="img" aria-label="Soft grey water droplet pattern"></div>
    <div class="brand-band">
      <div class="brand-mark">VS</div>
      <div class="brand-name">VELA SHIELD</div>
      <div class="brand-tagline">Antimicrobial Surface Protection</div>
    </div>
    <div class="texture texture--sky" role="img" aria-label="Pale blue water droplet pattern"></div>
  </section>

  <section class="card card--back">
    <div class="contact">
      <div class="contact__mark">VS</div>
      <p class="contact__line">Gareth Tolley</p>
      <p class="contact__line">velashieldnz@postbox.example</p>
      <p class="contact__line">+64219305562</p>
      <p class="contact__line">www.velashield.example.nz</p>
    </div>
    <div class="texture texture--fade" role="img" aria-label="Grey to blue water droplet pattern"></div>
  </section>
</main>
</body>
</html>
```